Business Card

We need some ideas for corporate business cards. I'm interested in a double sided card, with one side featuring our corporate logo, the other side with employee information.

Corporate colors, logo etc. available at www.brivalo.com

Industry/Entity Type

Business

Requirements
Must have
• The "Brivalo" logo with stylized "O"

Nice to have
• Preferred font is calibri

```html
<!DOCTYPE html>
<html lang="en">
<head>
<meta charset="utf-8">
<title>Brivalo Business Card</title>
<link rel="stylesheet" href="https://fonts.googleapis.com/css2?family=Open+Sans:wght@400;600;700&display=swap">
<style>
  :root {
    --page-bg: #d6d7d9;
    --card-white: #f7f7f7;
    --brand-blue: #3a5592;
    --band-blue: #445d9a;
    --back-blue: #3c5088;
    --brand-red: #9a1a31;
    --text-white: #ffffff;
  }
  * { margin: 0; padding: 0; box-sizing: border-box; }
  html, body {
    width: 1200px;
    height: 1000px;
    overflow: hidden;
    background: var(--page-bg);
    font-family: "Open Sans", Arial, sans-serif;
  }
  .canvas {
    position: relative;
    width: 1200px;
    height: 1000px;
  }
  .card {
    position: absolute;
    left: 320px;
    width: 560px;
    height: 320px;
    box-shadow: 0 6px 18px rgba(0, 0, 0, 0.18);
    overflow: hidden;
  }
  .card-back {
    top: 140px;
    background: var(--back-blue);
  }
  .card-back .wordmark {
    position: absolute;
    right: 56px;
    top: 118px;
    font-size: 78px;
    font-weight: 600;
    letter-spacing: 6px;
    color: var(--text-white);
    line-height: 1;
  }
  .card-front {
    top: 540px;
    background: var(--card-white);
  }
  .card-front .wordmark {
    position: absolute;
    left: 44px;
    top: 40px;
    font-size: 50px;
    font-weight: 600;
    letter-spacing: 4px;
    color: var(--brand-blue);
    line-height: 1;
  }
  .band {
    position: absolute;
    left: 0;
    top: 150px;
    width: 560px;
    height: 135px;
  }
  .contact {
    position: absolute;
    left: 38px;
    top: 156px;
    color: var(--text-white);
  }
  .contact .person-name {
    font-size: 22px;
    font-weight: 700;
    line-height: 1.2;
    margin-left: 12px;
  }
  .contact .designation {
    font-size: 14px;
    font-weight: 400;
    line-height: 1.2;
    margin-bottom: 12px;
  }
  .contact-row {
    display: flex;
    align-items: center;
    font-size: 14px;
    line-height: 20px;
  }
  .contact-row svg {
    width: 14px;
    height: 14px;
    margin-right: 10px;
    fill: var(--text-white);
  }
  .contact-row .sep { margin-right: 8px; }
</style>
</head>
<body>
<main class="canvas">
  <section class="card card-back" aria-label="Card back">
    <div class="wordmark">BRIVALO</div>
  </section>

  <section class="card card-front" aria-label="Card front">
    <div class="wordmark">BRIVALO</div>
    <svg class="band" viewBox="0 0 560 135" aria-hidden="true">
      <polygon points="0,0 470,0 420,135 0,135" fill="var(--band-blue)"/>
      <polygon points="482,0 560,0 560,135 432,135" fill="var(--brand-red)"/>
    </svg>
    <div class="contact">
      <p class="person-name">Person Name</p>
      <p class="designation">designation</p>
      <p class="contact-row">
        <svg viewBox="0 0 16 16" aria-label="Phone"><path d="M4 1h3l1 4-2 1.5c.8 1.8 2 3 3.6 3.6L11 8l4 1v3c0 1.2-1 2-2.2 1.8C7 13 3 9 2.2 3.2 2 2 2.8 1 4 1z"/></svg>
        <span class="sep">:</span>123 555 0142
      </p>
      <p class="contact-row">
        <svg viewBox="0 0 16 16" aria-label="Fax"><rect x="4" y="1" width="8" height="4"/><rect x="1" y="6" width="14" height="6" rx="1"/><rect x="4" y="11" width="8" height="4"/></svg>
        <span class="sep">:</span>123 555 0142
      </p>
      <p class="contact-row">
        <svg viewBox="0 0 16 16" aria-label="Email"><path d="M1 3h14v10H1z M1 3l7 6 7-6" fill="none" stroke="#fff" stroke-width="1.5"/></svg>
        <span class="sep">:</span>hello@brivalo.com
      </p>
    </div>
  </section>
</main>
</body>
</html>
```